Web Design Project

My site is already up - www.brightvale-hub.com but is very basic at this stage.
I need a to make the design look better and lift it a bit.
I have my own ideas about what I want.
The target market for the site is women - mainly professional, corporate women around the world aged between 28-40 yrs or thereabouts.
There are 3 main areas the site will focus on:
1: Blog and Inbox magazine with contributing writers on various topics from food, diet, emotional intelligence, intuition, feminine energy sexual and non, money to name a few.
2. There is an Ebook that is being added to the site later this year taking a deeper look at all of these topics. For now those subscribing get a free summary of the book.
Book called "Quiet Harbour - Your Gentle Map to a Calmer Day"
Happy to use the title for the FREE summary for subscribers.
3. Events / retreats. We are kicking off with our first Brightvale-hub retreat in Bali in late Oct 2012. We have amazing shots of the villa we will use and the activities etc that will make up a part of the retreat.
Yoga & meditation
Surfing
Photography
Keen to see what you all come up with.
NOTE: I dont want anything too busy. Keep it fairly clean, simple and in keeping with the general look and feel right now.
Target Market(s)
Look and feel
Each slider illustrates characteristics of the customer's brand and the style your logo design should communicate.

```html
<!DOCTYPE html>
<html lang="en">
<head>
<meta charset="utf-8">
<title>Brightvale-hub – a gentle map to a calmer day</title>
<link rel="stylesheet" href="https://fonts.googleapis.com/css2?family=Noto+Sans:wght@400;700&display=swap">
<style>
  :root {
    --yellow: #f7d70a;
    --white: #ffffff;
    --nav-bg: #ebebeb;
    --nav-text: #555555;
    --heading: #999999;
    --body: #666666;
    --muted: #8c8c8c;
    --rule: #e6e6e6;
    --frame: #e3e3e3;
    --header-link: #8a7a10;
    --map-border: #f5c55a;
    --btn: #dddddd;
  }
  * { box-sizing: border-box; margin: 0; padding: 0; }
  html, body { width: 1171px; height: 1200px; overflow: hidden; background: var(--white); }
  body { font-family: "Noto Sans", sans-serif; color: var(--body); position: relative; }
  .page { position: absolute; left: 46px; top: 0; width: 1079px; height: 1200px; }

  .site-header { position: absolute; top: 6px; left: 0; width: 1079px; height: 184px; background: var(--yellow); }
  .brand { position: absolute; left: 22px; top: 60px; display: flex; align-items: center; gap: 14px; }
  .brand-dot { width: 48px; height: 48px; border-radius: 50%; background: var(--white); }
  .brand-name { font-size: 40px; font-weight: 700; line-height: 1; color: var(--white); }
  .brand-tagline { position: absolute; left: 84px; top: 110px; font-size: 16px; color: #8a7a10; }
  .account { position: absolute; right: 24px; top: 33px; font-size: 12px; color: var(--header-link); }
  .search { position: absolute; right: 24px; top: 117px; width: 274px; height: 32px; background: var(--white); display: flex; align-items: center; padding: 0 16px; font-size: 13px; color: #aaaaaa; }
  .search svg { position: absolute; right: 4px; top: 4px; }

  .main-nav { position: absolute; top: 224px; left: 0; width: 1079px; height: 34px; background: var(--nav-bg); display: flex; padding-left: 23px; }
  .main-nav a { position: relative; font-size: 14px; font-weight: 700; color: var(--nav-text); text-decoration: none; line-height: 34px; margin-right: 46px; }
  .main-nav a.current::after { content: ""; position: absolute; left: 50%; bottom: 0; margin-left: -6px; border: 6px solid transparent; border-bottom-color: var(--nav-text); border-top: 0; }

  .rule { position: absolute; left: 0; width: 1079px; height: 1px; background: var(--rule); }

  .feature { position: absolute; top: 327px; width: 300px; }
  .feature-frame { width: 298px; height: 224px; background: var(--frame); padding: 11px; }
  .feature-photo { width: 100%; height: 100%; }
  .feature h2 { margin-top: 38px; width: 250px; font-size: 34px; font-weight: 400; color: var(--heading); line-height: 36px; }
  .feature p { margin-top: 22px; font-size: 14px; line-height: 28.7px; color: var(--body); width: 290px; }

  .contact { position: absolute; top: 877px; font-size: 12.5px; line-height: 21.8px; color: var(--body); }
  .contact h3, .footer-col h3 { font-size: 16px; font-weight: 400; color: var(--muted); margin-bottom: 10px; }
  .map { width: 197px; height: 104px; border: 2px solid var(--map-border); background: linear-gradient(135deg, #efeae0, #e2dccd); }

  .footer-col { position: absolute; top: 1086px; }
  .newsletter { width: 287px; height: 37px; border: 1px solid var(--rule); display: flex; align-items: center; justify-content: space-between; padding: 0 4px 0 10px; font-size: 14px; color: #aaaaaa; }
  .newsletter span.btn { background: var(--btn); color: #777777; font-weight: 700; font-size: 14px; padding: 2px 12px; }
  .footer-col p { font-size: 12.5px; line-height: 21.8px; color: var(--muted); }
  .social { display: flex; gap: 14px; margin-top: 6px; }
  .social span { width: 44px; height: 44px; border-radius: 8px; }
  .s1 { background: #7fd0ec; } .s2 { background: #4a6ea8; } .s3 { background: #dcdcdc; } .s4 { background: #f29a2e; }
</style>
</head>
<body>
<div class="page">
  <header class="site-header">
    <div class="brand"><span class="brand-dot"></span><span class="brand-name">Brightvale-hub</span></div>
    <div class="brand-tagline">A gentle map to a calmer day</div>
    <div class="account">You are not logged in &nbsp;|&nbsp; Login or Register</div>
    <div class="search">search
      <svg width="26" height="26" viewBox="0 0 26 26" fill="none" stroke="#999" stroke-width="1.6"><circle cx="11" cy="11" r="7.5"/><line x1="16.5" y1="16.5" x2="23" y2="23"/></svg>
    </div>
  </header>

  <nav class="main-nav">
    <a class="current" href="#">Home</a><a href="#">About</a><a href="#">Blog</a><a href="#">Community</a><a href="#">Retreats</a><a href="#">Contact</a>
  </nav>

  <div class="rule" style="top:293px"></div>

  <article class="feature" style="left:0">
    <div class="feature-frame" style="background:#dfe6c8"><div class="feature-photo" role="img" aria-label="Woman relaxing on a blanket in a sunny park" style="background:linear-gradient(180deg,#5f8a3a,#7aa94a 55%,#8fb85a)"></div></div>
    <h2>Curabitur in metus</h2>
    <p>Lorem ipsum dolor sit amet, consectetur adipiscing elit. Mauris tincidunt arcu a ipsum congue mattis. Donec iaculis risus ornare lorem bibendum facilisis. Morbi ut tempus nunc. Cras sollicitudin dapibus</p>
  </article>

  <article class="feature" style="left:390px">
    <div class="feature-frame"><div class="feature-photo" role="img" aria-label="Bundle of rhubarb stalks tied with string" style="background:radial-gradient(ellipse at center,#e86a6a 0%,#f2a3a0 40%,#ffffff 75%)"></div></div>
    <h2>Curabitur in metus</h2>
    <p>Lorem ipsum dolor sit amet, consectetur adipiscing elit. Mauris tincidunt arcu a ipsum congue mattis. Donec iaculis risus ornare lorem bibendum facilisis. Morbi ut tempus nunc. Cras sollicitudin dapibus</p>
  </article>

  <article class="feature" style="left:782px">
    <div class="feature-frame" style="background:#c9d0da"><div class="feature-photo" role="img" aria-label="Engineer in a hard hat holding plans at an industrial site" style="background:linear-gradient(180deg,#3d7fd0,#7aa8e0 60%,#9a9a9a)"></div></div>
    <h2>Curabitur in metus</h2>
    <p>Lorem ipsum dolor sit amet, consectetur adipiscing elit. Mauris tincidunt arcu a ipsum congue mattis. Donec iaculis risus ornare lorem bibendum facilisis. Morbi ut tempus nunc. Cras sollicitudin dapibus</p>
  </article>

  <div class="rule" style="top:851px"></div>

  <section class="contact" style="left:0">
    <h3>Massa:</h3>
    3358 Etiam Consequat<br>Sodales 2727 Etiam Dapibus<br>Phone: (01) 5885 1424<br>Fax: (01) 5885 1425<br>Email: quisque@tincidunt.ut
  </section>
  <section class="contact" style="left:390px">
    <h3>How to find us:</h3>
    <div class="map" role="img" aria-label="Street map showing the office location"></div>
  </section>
  <section class="contact" style="left:782px">
    <h3>Mauris:</h3>
    3358 Etiam Consequat<br>Sodales 2727 Etiam Dapibus<br>Phone: (01) 5885 1424<br>Fax: (01) 5885 1425<br>Email: quisque@tincidunt.ut
  </section>

  <div class="rule" style="top:1060px"></div>

  <section class="footer-col" style="left:0">
    <h3>Subscribe to our newsletter</h3>
    <div class="newsletter">you@example.com<span class="btn">Sign up</span></div>
  </section>
  <section class="footer-col" style="left:390px">
    <h3>Harbourline HR Services</h3>
    <p>Vestibulum ligula justo, ultricies<br>A iaculis at, cursus quis lacus. Proin vitae mauris</p>
  </section>
  <section class="footer-col" style="left:827px">
    <h3>Follow us</h3>
    <div class="social"><span class="s1"></span><span class="s2"></span><span class="s3"></span><span class="s4"></span></div>
  </section>
</div>
</body>
</html>
```